WP website design for Colbury

We need a wordpress design for an established auction and real estate company based in New Jersey. The winning design will incorporate a professional color scheme with company logo in a clean layout. The design needs to consider that this will be developed on a responsive theme. Colors are those that will highlight the logo

Industry/Entity Type

Real Estate

Font styles to use
Serif
Sans Serif

Requirements
Must have
• colors will be #3E3D5D and #3C7296
navigation: 1) Home 2) Auctions 3) Real Estate Listings 4) Buyers 5) Sellers 6) About Us 7 ) Contact Us
design will use a slideshow - image is attached.
Widgets to place in the header, sidebar or footer:
1) email signup form 2) social icons (facebook, twitter, youtube, RSS) 3) Featured Properties widget 4) Featured Auctions widget 5) News & Events blog 6) Featured Videos
Nice to have
• Site will have numerous dropdown menus - so it would be nice to have a sample of what the dropdowns would look like. EG 1)▪ Our Featured Listings and 2)▪ MLS Property Search under the main "Real Estate Listings" menu item.

```html
<!DOCTYPE html>
<html lang="en">
<head>
<meta charset="utf-8">
<title>Colbury Real Estate &amp; Auction</title>
<link href="https://fonts.googleapis.com/css2?family=Open+Sans:wght@400;600;700&display=swap" rel="stylesheet">
<style>
:root{
  --blue:#3C7296;
  --navy:#3E3D5D;
  --navy-dark:#2f2e48;
  --green:#8cc63f;
  --text:#333;
  --muted:#555;
  --line:#d9d9d9;
  --panel:#efefef;
  --white:#fff;
}
*{margin:0;padding:0;box-sizing:border-box}
html,body{width:741px;height:1200px;overflow:hidden}
body{position:relative;font-family:"Open Sans",Arial,sans-serif;color:var(--text);background:var(--white)}
.abs{position:absolute}

/* top bar */
.topbar{left:0;top:0;width:741px;height:37px;background:var(--blue)}
.topbar a{position:absolute;top:11px;font-size:10px;color:var(--white);text-decoration:none}
.social-dot{position:absolute;top:11px;width:13px;height:13px;border-radius:50%;background:var(--white)}

/* header */
.header{left:0;top:37px;width:741px;height:53px;background:var(--white)}
.brand{position:absolute;left:29px;top:8px;display:flex;align-items:center;gap:6px}
.brand-mark{width:14px;height:14px;background:var(--blue)}
.brand-name{font-size:15px;font-weight:700;color:var(--navy)}
.nav a{position:absolute;top:13px;font-size:11.5px;color:var(--navy);text-decoration:none;white-space:nowrap}
.nav a.active{color:var(--blue)}
.dropdown{left:337px;top:90px;width:127px;height:43px;background:var(--white);box-shadow:0 2px 4px rgba(0,0,0,.15);z-index:3}
.dropdown a{display:block;height:21px;line-height:21px;padding-left:8px;font-size:8.5px;color:var(--blue);text-decoration:none}
.dropdown a+a{background:#e9e9e9}

/* hero */
.hero{left:0;top:90px;width:741px;height:267px;background:linear-gradient(180deg,#7fb0e0 0%,#c9dff0 45%,#8fae5a 72%,#4e8a2a 100%)}
.hero-arrow{left:27px;top:197px}
.slide-card{left:61px;top:173px;width:346px;height:144px;background:rgba(60,114,150,.82);color:var(--white);padding:12px 15px}
.slide-card h1{font-size:26px;font-weight:400;line-height:1.1}
.slide-card p{margin-top:14px;font-size:8px;line-height:1.3;width:310px}
.price-tag{position:absolute;left:15px;top:108px;width:93px;height:27px;background:var(--green);color:var(--white);font-size:17px;line-height:27px;padding-left:8px}

/* sections */
.section-title{font-size:13px;font-weight:600;color:var(--text)}
.card{width:235px;height:243px;border:1px solid var(--line);background:var(--white);box-shadow:0 1px 2px rgba(0,0,0,.08)}
.card .photo{position:absolute;left:11px;top:7px;width:212px;height:134px;background:linear-gradient(180deg,#2f6fc4 0%,#8fb8e6 55%,#7a9a5a 80%,#5b7a3c 100%)}
.card h3{position:absolute;left:11px;top:147px;font-size:9.5px;font-weight:400;color:var(--text)}
.card p{position:absolute;left:11px;top:162px;width:214px;font-size:7.5px;line-height:1.35;color:var(--muted)}
.card .price{position:absolute;left:11px;top:212px;font-size:17px;color:var(--text)}
.card .more{position:absolute;left:160px;top:221px;width:64px;height:16px;background:var(--green);color:var(--white);font-size:8px;line-height:16px;text-align:center}

.feature{width:201px;height:52px;border:1px solid var(--line);background:var(--panel);box-shadow:0 1px 2px rgba(0,0,0,.1)}
.feature .thumb{position:absolute;left:2px;top:5px;width:55px;height:42px;background:linear-gradient(180deg,#7fa7cf,#b9643e 60%,#8a6c55)}
.feature .name{position:absolute;left:68px;top:8px;font-size:9.5px;color:var(--text)}
.feature .amount{position:absolute;left:68px;top:22px;font-size:17px;color:var(--green)}

/* partners */
.partners{left:0;top:917px;width:741px;height:74px;background:linear-gradient(90deg,#1e1e22,#4a4a4e 50%,#1e1e22)}
.badge-strip{left:208px;top:928px;width:325px;height:56px;background:#d6d6d6;display:flex;align-items:center;justify-content:space-around;padding:0 18px}
.badge{height:34px;background:#333}

/* footer */
.footer{left:0;top:991px;width:741px;height:185px;background:var(--navy);color:var(--white)}
.footer h4{position:absolute;top:13px;font-size:13px;font-weight:400;white-space:nowrap}
.footer .small{font-size:8.5px;line-height:1.3}
.video-thumb{left:29px;top:64px;width:142px;height:101px;background:linear-gradient(180deg,#9cc0e0,#d8dfe4 55%,#7c8f74)}
.social-list{width:120px;height:185px}
.social-list div{position:absolute;left:24px;font-size:9px;white-space:nowrap;line-height:12px}
.social-list span.ico{position:absolute;left:-24px;top:0;width:12px;height:12px;border-radius:50%;background:var(--white)}
.field{position:absolute;left:573px;width:138px;height:19px;background:#e8e8ee;font-size:8px;color:#888;font-style:italic;padding:4px 5px}
.signup-btn{position:absolute;left:573px;top:120px;width:138px;height:21px;background:var(--blue);font-size:9px;line-height:21px;text-align:center}
.copyright{left:0;top:1176px;width:741px;height:24px;background:var(--navy-dark);color:#b9b8d0;font-size:7.5px;line-height:24px;padding-left:29px}
.to-top{position:absolute;right:13px;top:7px;width:10px;height:10px;border-radius:50%;border:2px solid #9b9ac0}
</style>
</head>
<body>

<div class="abs topbar">
  <a href="#" style="left:37px">Login</a>
  <a href="#" style="left:85px">Register</a>
  <span class="social-dot" style="left:613px"></span>
  <span class="social-dot" style="left:638px"></span>
  <span class="social-dot" style="left:665px"></span>
  <span class="social-dot" style="left:692px"></span>
</div>

<header class="abs header">
  <div class="brand"><span class="brand-mark"></span><span class="brand-name">Colbury</span></div>
  <nav class="nav">
    <a href="#" style="left:225px">Home</a>
    <a href="#" style="left:280px">Auctions</a>
    <a href="#" class="active" style="left:345px">Real Estate Listings
      <svg width="9" height="6" viewBox="0 0 9 6" style="margin-left:4px"><path d="M1 1l3.5 3.5L8 1" fill="none" stroke="#3C7296" stroke-width="1.6"/></svg></a>
    <a href="#" style="left:476px">Buyers</a>
    <a href="#" style="left:535px">Sellers</a>
    <a href="#" style="left:593px">About Us</a>
    <a href="#" style="left:663px">Contact Us</a>
  </nav>
</header>

<section class="abs hero" role="img" aria-label="Farm with green fields, barns and silos under a blue sky"></section>
<svg class="abs hero-arrow" width="16" height="22" viewBox="0 0 16 22"><path d="M13 2L4 11l9 9" fill="none" stroke="#fff" stroke-width="4"/></svg>
<div class="abs slide-card">
  <h1>Duis Vitae Tempor Mi</h1>
  <p>Fusce aliquet euismod leo, non luctus felis volutpat ac. In suscipit libero magna, quis egestas felis elementum a. Maecenas malesuada nibh at dignissim fermentum. Nulla ac euismod urna</p>
  <div class="price-tag">$ 345,000</div>
</div>

<nav class="abs dropdown">
  <a href="#">Our Featured Listings</a>
  <a href="#">MLS Property Search</a>
</nav>

<h2 class="abs section-title" style="left:29px;top:371px">Recent Properties</h2>

<article class="abs card" style="left:29px;top:399px">
  <div class="photo" role="img" aria-label="Two-storey suburban house with garage"></div>
  <h3>Praesent vulputate est in dui</h3>
  <p>Morbi ullamcorper vel mauris eu vulputate. Proin felis nunc, feugiat volutpat lobortis in, convallis vel ligula. Phasellus at tempus neque. Donec arcu tortor, viverra non facilisis et, ullamcorper sed nisi ...</p>
  <div class="price">$ 321,000</div><div class="more">More ...</div>
</article>
<article class="abs card" style="left:268px;top:399px">
  <div class="photo" role="img" aria-label="Two-storey suburban house with garage"></div>
  <h3>Praesent vulputate est in dui</h3>
  <p>Morbi ullamcorper vel mauris eu vulputate. Proin felis nunc, feugiat volutpat lobortis in, convallis vel ligula. Phasellus at tempus neque. Donec arcu tortor, viverra non facilisis et, ullamcorper sed nisi ...</p>
  <div class="price">$ 321,000</div><div class="more">More ...</div>
</article>
<article class="abs card" style="left:29px;top:650px">
  <div class="photo" role="img" aria-label="Two-storey suburban house with garage"></div>
  <h3>Praesent vulputate est in dui</h3>
  <p>Morbi ullamcorper vel mauris eu vulputate. Proin felis nunc, feugiat volutpat lobortis in, convallis vel ligula. Phasellus at tempus neque. Donec arcu tortor, viverra non facilisis et, ullamcorper sed nisi ...</p>
  <div class="price">$ 321,000</div><div class="more">More ...</div>
</article>
<article class="abs card" style="left:268px;top:650px">
  <div class="photo" role="img" aria-label="Two-storey suburban house with garage"></div>
  <h3>Praesent vulputate est in dui</h3>
  <p>Morbi ullamcorper vel mauris eu vulputate. Proin felis nunc, feugiat volutpat lobortis in, convallis vel ligula. Phasellus at tempus neque. Donec arcu tortor, viverra non facilisis et, ullamcorper sed nisi ...</p>
  <div class="price">$ 321,000</div><div class="more">More ...</div>
</article>

<h2 class="abs section-title" style="left:511px;top:371px">Featured Properties</h2>
<div class="abs feature" style="left:511px;top:405px"><div class="thumb" role="img" aria-label="Modern apartment building"></div><div class="name">Sed eget sagittis nisi</div><div class="amount">$ 123,000</div></div>
<div class="abs feature" style="left:511px;top:463px"><div class="thumb" role="img" aria-label="Modern apartment building"></div><div class="name">Sed eget sagittis nisi</div><div class="amount">$ 123,000</div></div>
<div class="abs feature" style="left:511px;top:521px"><div class="thumb" role="img" aria-label="Modern apartment building"></div><div class="name">Sed eget sagittis nisi</div><div class="amount">$ 123,000</div></div>

<h2 class="abs section-title" style="left:511px;top:625px">Featured Auctions</h2>
<div class="abs feature" style="left:511px;top:655px"><div class="thumb" role="img" aria-label="Modern apartment building"></div><div class="name">Sed eget sagittis nisi</div><div class="amount">$ 123,000</div></div>
<div class="abs feature" style="left:511px;top:713px"><div class="thumb" role="img" aria-label="Modern apartment building"></div><div class="name">Sed eget sagittis nisi</div><div class="amount">$ 123,000</div></div>
<div class="abs feature" style="left:511px;top:771px"><div class="thumb" role="img" aria-label="Modern apartment building"></div><div class="name">Sed eget sagittis nisi</div><div class="amount">$ 123,000</div></div>

<section class="abs partners" role="img" aria-label="Auction gavel on a dark wooden desk"></section>
<div class="abs badge-strip" aria-label="Partner associations">
  <span class="badge" style="width:28px"></span>
  <span class="badge" style="width:28px"></span>
  <span class="badge" style="width:66px"></span>
  <span class="badge" style="width:88px"></span>
</div>

<footer class="abs footer">
  <h4 style="left:29px">Featured Videos</h4>
  <div class="abs small" style="left:29px;top:40px">Sed eu nunc lacus</div>
  <div class="abs video-thumb" role="img" aria-label="Video preview of a modern house"></div>
  <svg class="abs" style="left:84px;top:101px" width="34" height="26" viewBox="0 0 34 26"><rect width="34" height="26" rx="5" fill="rgba(255,255,255,.55)"/><path d="M13 7l10 6-10 6z" fill="#fff"/></svg>

  <h4 style="left:193px">News and Events</h4>
  <div class="abs small" style="left:193px;top:37px;width:220px">
    <div style="font-size:9.5px">Nunc vulputate tempor tincidunt event</div>
    <div style="margin-top:3px">Donec tincidunt commodo mi ac imperdiet. Praesent vitae adipiscing ipsum</div>
    <div style="margin:4px 0 0 14px">Date&nbsp;&nbsp;: Monday 23 March 2014<br>Time : 9.00am - 3.00pm<br>Cost&nbsp;&nbsp;: $ 100</div>
    <div style="font-size:9.5px;margin-top:4px">Lorem Ipsum</div>
    <div style="margin-top:2px">Maecenas et nisi lacinia, vehicula nunc vel, aliquam nibh. Aliquam erat volutpat. Integer ac malesuada enim. Etiam iaculis ...more</div>
  </div>

  <h4 style="left:437px">Social Links</h4>
  <div class="social-list abs" style="left:441px;top:0">
    <div style="top:54px"><span class="ico"></span>Community URL</div>
    <div style="top:82px"><span class="ico"></span>Updates URL</div>
    <div style="top:110px"><span class="ico"></span>Video URL</div>
    <div style="top:138px"><span class="ico"></span>RSS Feed</div>
  </div>

  <h4 style="left:568px">Signup Form</h4>
  <div class="field" style="top:53px">Your Name</div>
  <div class="field" style="top:88px">Your email</div>
  <div class="signup-btn">Signup</div>
</footer>

<div class="abs copyright">Copyright 2014 | Colbury. All Rights Reserved<span class="to-top"></span></div>

</body>
</html>
```